Harbinger Slabworks, Inc. Business Card

Create a business card that is eye catching and based around concrete sawcutting. I've attached our current business card and logo for reference. We like aspects of the current business card, but it is starting to feel very loud and lost. We would like something that is still fun but is more modern and streamlined.

```html
<!DOCTYPE html>
<html lang="en">
<head>
<meta charset="utf-8">
<title>Harbinger Slabworks, Inc. Business Card</title>
<link rel="stylesheet" href="https://fonts.googleapis.com/css2?family=Montserrat:wght@400;700;800&family=Open+Sans:wght@400;600&family=Oswald:wght@600&display=swap">
<style>
  :root {
    --page-bg: #2a2b2d;
    --card-black: #1c1c1e;
    --plate-dark: #232325;
    --plate-light: #3a3b3e;
    --signal-red: #e01b24;
    --steel-light: #e9eaec;
    --steel-mid: #a9acb1;
    --steel-dark: #6c6f74;
    --text-white: #f2f2f2;
    --text-grey: #b9b9bb;
  }
  * { box-sizing: border-box; margin: 0; padding: 0; }
  html, body { width: 1200px; height: 1200px; overflow: hidden; }
  body {
    background: var(--page-bg);
    font-family: "Open Sans", sans-serif;
    position: relative;
  }
  .card {
    position: absolute;
    top: 215px;
    width: 440px;
    height: 770px;
    border-radius: 28px;
    overflow: hidden;
  }
  .card--front { left: 120px; background: var(--card-black); }
  .card--back { left: 640px; }

  /* Front */
  .steel-tab {
    position: absolute;
    left: 95px; top: 0;
    width: 250px; height: 92px;
    background: linear-gradient(90deg, var(--steel-dark), var(--steel-light) 45%, var(--steel-mid) 70%, var(--steel-light));
  }
  .brand {
    position: absolute;
    left: 0; right: 0;
    display: flex; flex-direction: column; align-items: center;
    font-family: "Montserrat", sans-serif;
    font-weight: 800;
    color: var(--steel-light);
    text-transform: uppercase;
    text-align: center;
    letter-spacing: 2px;
  }
  .brand-dot {
    width: 150px; height: 150px;
    border-radius: 50%;
    border: 10px solid var(--signal-red);
    margin-bottom: 18px;
  }
  .brand-name { font-size: 26px; line-height: 1.2; }
  .card--front .brand { top: 120px; }

  .person { position: absolute; top: 440px; left: 0; right: 0; text-align: center; }
  .person-name {
    font-family: "Montserrat", sans-serif;
    font-weight: 700;
    font-size: 27px;
    color: var(--signal-red);
    text-transform: uppercase;
  }
  .person-role { font-size: 14px; color: var(--text-grey); margin-top: 2px; }

  .contact-icons {
    position: absolute; top: 512px; left: 0; right: 0;
    display: flex; justify-content: center; align-items: center; gap: 7px;
  }
  .rule { width: 62px; height: 2px; background: var(--signal-red); margin: 0 14px; }
  .icon {
    width: 20px; height: 20px; border-radius: 4px;
    background: var(--signal-red);
    display: flex; align-items: center; justify-content: center;
  }
  .contact-lines {
    position: absolute; top: 548px; left: 0; right: 0;
    text-align: center; color: var(--text-white);
    font-size: 15.5px; line-height: 1.45;
  }
  .short-rule {
    position: absolute; top: 665px; left: 190px;
    width: 60px; height: 2px; background: var(--signal-red);
  }
  .address {
    position: absolute; top: 682px; left: 0; right: 0;
    text-align: center; color: var(--text-white);
    font-size: 15.5px; line-height: 1.45;
  }

  /* Back */
  .plate {
    position: absolute; inset: 0;
    background: radial-gradient(ellipse at 55% 35%, var(--plate-light), var(--plate-dark) 75%);
  }
  .card--back .brand { top: 150px; }
  .services { position: absolute; top: 520px; left: 130px; }
  .services-title {
    font-family: "Oswald", sans-serif;
    font-weight: 600;
    font-size: 30px;
    letter-spacing: 1px;
    text-transform: uppercase;
    background: linear-gradient(180deg, var(--steel-light), var(--steel-mid));
    -webkit-background-clip: text; background-clip: text;
    color: transparent;
    margin-bottom: 14px;
  }
  .services-list { list-style: none; padding-left: 10px; }
  .services-list li {
    font-family: "Montserrat", sans-serif;
    font-weight: 700;
    font-size: 17px;
    color: var(--text-white);
    line-height: 1.6;
    display: flex; align-items: center; gap: 12px;
  }
  .services-list li::before {
    content: ""; width: 6px; height: 6px; border-radius: 50%;
    background: var(--steel-light);
  }
</style>
</head>
<body>
  <section class="card card--front">
    <div class="steel-tab"></div>
    <div class="brand">
      <span class="brand-dot"></span>
      <span class="brand-name">Harbinger<br>Slabworks</span>
    </div>
    <div class="person">
      <h1 class="person-name">Dana Whitfield</h1>
      <p class="person-role">Owner</p>
    </div>
    <div class="contact-icons">
      <span class="rule"></span>
      <span class="icon"><svg width="12" height="12" viewBox="0 0 12 12"><path d="M2.5 1 4.5 1 5.3 3.6 4 4.6Q5 7 7.4 8L8.4 6.7 11 7.5 11 9.5Q11 11 9.5 11 1 10 1 2.5 1 1 2.5 1Z" fill="#fff"/></svg></span>
      <span class="icon"><svg width="12" height="12" viewBox="0 0 12 12"><rect x="3" y="1" width="6" height="10" rx="1" fill="#fff"/><rect x="4" y="2.5" width="4" height="6" fill="#e01b24"/></svg></span>
      <span class="icon"><svg width="12" height="12" viewBox="0 0 12 12"><rect x="1" y="3" width="10" height="7" fill="#fff"/><path d="M1 3 6 7 11 3" stroke="#e01b24" fill="none"/></svg></span>
      <span class="icon"><svg width="12" height="12" viewBox="0 0 12 12"><circle cx="6" cy="6" r="4.5" fill="none" stroke="#fff" stroke-width="1.3"/><path d="M1.5 6H10.5M6 1.5Q3.5 6 6 10.5M6 1.5Q8.5 6 6 10.5" stroke="#fff" fill="none"/></svg></span>
      <span class="rule"></span>
    </div>
    <div class="contact-lines">
      <p>(855) 410-3362</p>
      <p>855-CUT-SLAB</p>
      <p>dana@harbingerslabworks.com</p>
      <p>www.harbingerslabworks.com</p>
    </div>
    <div class="short-rule"></div>
    <div class="address">
      <p>48 North Alder Street,</p>
      <p>Fairhaven, NJ 07704</p>
    </div>
  </section>

  <section class="card card--back">
    <div class="plate" role="img" aria-label="Dark steel diamond tread plate texture"></div>
    <div class="brand">
      <span class="brand-dot"></span>
      <span class="brand-name">Harbinger<br>Slabworks</span>
    </div>
    <div class="services">
      <h2 class="services-title">Our Services</h2>
      <ul class="services-list">
        <li>Wall Sawing</li>
        <li>Core Drilling</li>
        <li>Slab Sawing</li>
        <li>Breaking &nbsp;Removal</li>
      </ul>
    </div>
  </section>
</body>
</html>
```